Business Cards/Stationary for CIO Outsourcing Company
Velmora Solutions
Use same font as used in my logo
Dorian Halbrook
Partner
Four Maple Ridge Plaza
Suite 240
Alderbrook, Westland 00240
dhalbrook@govelmora.com
www.govelmora.com
Logo icon can be shown separate from the name if necessary on stationary.

```html
<!DOCTYPE html>
<html lang="en">
<head>
<meta charset="utf-8">
<title>Velmora Solutions – Business Card</title>
<link rel="stylesheet" href="https://fonts.googleapis.com/css2?family=Cinzel:wght@400;600&display=swap">
<style>
  :root {
    --stage: #e4e4e4;
    --card-white: #fbfbfb;
    --brand-red: #c0252d;
    --brand-red-deep: #a81e26;
    --ink: #3a3a3a;
    --ink-soft: #6a6a6a;
    --swoosh-dark: #2b2b2b;
    --swoosh-grey: #b9b9b9;
    --back-text: rgba(255,255,255,0.75);
  }
  * { box-sizing: border-box; margin: 0; padding: 0; }
  html, body { width: 1200px; height: 980px; overflow: hidden; }
  body {
    background: var(--stage);
    font-family: "Cinzel", "Times New Roman", serif;
    position: relative;
  }
  .card {
    position: absolute;
    width: 700px;
    height: 400px;
    border-radius: 26px;
    overflow: hidden;
    box-shadow: 0 10px 28px rgba(0,0,0,0.18);
  }
  /* Back side */
  .card-back {
    left: 430px;
    top: 80px;
    background: linear-gradient(160deg, var(--brand-red) 0%, var(--brand-red-deep) 100%);
  }
  .card-back .web {
    position: absolute;
    left: 44px;
    top: 56px;
    font-size: 15px;
    letter-spacing: 7px;
    color: var(--back-text);
  }
  .card-back .brand-circle {
    position: absolute;
    right: 60px;
    top: 120px;
    width: 200px;
    height: 200px;
    border-radius: 50%;
    background: rgba(255,255,255,0.12);
  }
  /* Front side */
  .card-front {
    left: 70px;
    top: 500px;
    background: var(--card-white);
  }
  .card-front .swoosh {
    position: absolute;
    inset: 0;
  }
  .brand {
    position: absolute;
    left: 180px;
    top: 70px;
    display: flex;
    align-items: center;
    gap: 14px;
  }
  .brand-mark {
    width: 46px;
    height: 46px;
    border-radius: 50%;
    background: var(--brand-red);
  }
  .brand-name {
    font-size: 50px;
    font-weight: 400;
    color: var(--brand-red);
    letter-spacing: 2px;
    line-height: 1;
  }
  .identity {
    position: absolute;
    right: 370px;
    top: 160px;
    text-align: right;
    font-size: 12px;
    line-height: 19px;
    color: var(--ink);
  }
  .identity .person { color: var(--brand-red); }
  .identity .role { color: var(--ink-soft); margin-bottom: 12px; }
  .contact {
    position: absolute;
    left: 344px;
    top: 160px;
    list-style: none;
    font-size: 12px;
    line-height: 19px;
    color: var(--ink);
  }
  .contact li { display: flex; align-items: center; gap: 10px; }
  .contact .dot {
    width: 11px;
    height: 11px;
    border-radius: 50%;
    background: var(--brand-red);
    flex: none;
  }
</style>
</head>
<body>

  <section class="card card-back" aria-label="Business card, back">
    <p class="web">www.govelmora.com</p>
    <div class="brand-circle"></div>
  </section>

  <section class="card card-front" aria-label="Business card, front">
    <svg class="swoosh" width="700" height="400" viewBox="0 0 700 400" aria-hidden="true">
      <path d="M0,300 C170,352 420,386 700,397 L700,400 L0,400 Z" fill="var(--brand-red)"/>
      <path d="M0,282 C170,340 420,374 700,388" fill="none" stroke="var(--swoosh-dark)" stroke-width="4"/>
      <path d="M0,268 C180,326 430,360 700,374" fill="none" stroke="var(--swoosh-grey)" stroke-width="2"/>
    </svg>

    <div class="brand">
      <span class="brand-mark"></span>
      <span class="brand-name">VELMORA</span>
    </div>

    <div class="identity">
      <p class="person">Dorian Halbrook</p>
      <p class="role">Partner</p>
      <p>Four Maple Ridge Plaza</p>
      <p>Suite 240 Alderbrook, Westland 00240</p>
    </div>

    <ul class="contact">
      <li><span class="dot"></span>(555) 010-0142</li>
      <li><span class="dot"></span>(555) 010-0187</li>
      <li><span class="dot"></span>dhalbrook@govelmora.com</li>
      <li><span class="dot"></span>www.govelmora.com</li>
    </ul>
  </section>

</body>
</html>
```